Letterhead Design for Vostrana Corporate Stationery

We are seeking a talented designer on ArtHarbor to create a professional and cohesive corporate stationery set for our company, Vostrana. Vostrana is a prominent player in the Commercial Real Estate industry, and we need stationery that reflects our brand's excellence and professionalism.

Scope of Work:

1. Letterhead Template (Microsoft Word):

Design a letterhead template in Microsoft Word format that adheres to our brand standards (attached in project files).
Include all necessary elements such as company logo, address, contact information, and any other relevant details.
The letterhead should be clean, elegant, and suitable for official business correspondence.

2. Business Cards:

Design business cards for our team members using the provided brand guidelines.
Include name, title, contact information, and the Vostrana logo.
Create a design that leaves a lasting impression and reflects our brand's professionalism.

3. Envelopes:

Design envelopes in various sizes (e.g., standard letter and legal sizes) that match the overall stationery theme.
Ensure that the design includes our company name, logo, and return address in accordance with brand guidelines.

4. Stationery:

Create a visually appealing stationery template that can be used for various documents and correspondence.
Ensure that the stationery design aligns with our brand standards and maintains consistency across all materials.

Submission Requirements:

Provide high-resolution files for each item (letterhead, business cards, envelopes, and stationery) in formats suitable for both print and digital use.
Include editable source files (e.g., Adobe Illustrator, Photoshop) for future modifications if necessary.

Design Guidelines:

Our brand is known for professionalism, trustworthiness, and excellence in the Commercial Real Estate industry. Please adhere to the brand standards provided in the project attachments.
Use our company colors, fonts, and logo as specified in the brand guidelines.
Feel free to be creative within the boundaries of our brand to make our stationery stand out while maintaining a professional look.

Budget and Timeline:

We are looking for high-quality designs at a competitive price.
The project timeline is flexible, but we would appreciate prompt responses from designers.
Please submit your best pricing and estimated delivery times with your proposals.
We look forward to receiving your creative and professional designs that will represent Vostrana in the best possible light. Thank you for considering our project, and we can't wait to see your submissions on ArtHarbor!

Target Market(s)

Our primary target market for the corporate stationery design project includes, but is not limited to: Investors: Individuals or entities interested in commercial real estate investment opportunities. Brokers: Commercial real estate brokers who facilitate property transactions and negotiations. Tenant Representatives: Professionals who advocate for the interests of tenants in commercial lease transactions. Lenders: Financial institutions and lenders involved in providing financing for commercial real estate projects. Property Owners: Owners of commercial real estate properties seeking professional correspondence materials. Industry Partners: Professionals and organizations within the commercial real estate industry who collaborate with or provide services to Vostrana. Prospective Clients: Potential clients or partners exploring opportunities in the commercial real estate sector. Please note that while these are the primary target market segments, the stationery design should also appeal to a broader audience within the commercial real estate industry and convey professionalism and trustworthiness to all stakeholders.

Industry/Entity Type

Commercial Real Estate

Font styles to use
Sans Serif

Colors
0054AA
0677BA
7BADD7
CADEEF
E8F1F8
0094D4
00A9DD
6FCCEA
C7EBF8
E9F6FB
F0912C
F2A743
F7CA91
FBE8D2
FDF5EE
EE7325
F08F49
F5BC92
FAE3D3
FDF4ED

Requirements
Must have
• Brand Consistency: Ensure that the design adheres to Vostrana's existing brand standards and guidelines (provided in project attachments). Professional Appearance: The stationery must convey professionalism, trustworthiness, and excellence in the Commercial Real Estate industry. Logo Usage: Integrate the Vostrana logo prominently and appropriately on all stationery items. Contact Information: Include accurate contact details, such as the company's address, phone number, email address, and website URL. Typography: Use the specified fonts from the brand guidelines for all text elements, maintaining consistency in font style and size. Color Palette: Utilize the designated brand colors consistently throughout the design. File Formats: Ensure that the final design files are provided in high-resolution formats suitable for both print and digital use. Also, request editable source files (e.g., Adobe Illustrator, Photoshop) for future modifications if needed. Print-Ready: Prepare the design files to be print-ready, including the appropriate bleed and margin specifications for printing purposes. Stationery Variations: Include designs for letterhead, business cards, envelopes (multiple sizes if applicable), and general stationery. Creativity within Brand Guidelines: Encourage designers to be creative while working within the boundaries of Vostrana's brand standards, making the stationery unique and eye-catching. Versatility: Ensure that the stationery can be easily adapted for various purposes, such as formal business correspondence, presentations, and more. Timely Delivery: Specify your preferred timeline for receiving initial design concepts and revisions. Budget: Indicate your budget range for the project to attract designers who can provide high-quality work within your financial constraints. Responsive Designers: Request that designers are responsive to messages and able to make necessary revisions in a timely manner.
Nice to have
• Creative Elements: Incorporate unique and creative design elements that align with Vostrana's brand identity and the Commercial Real Estate industry. Texture or Embossing: If applicable and within budget, consider incorporating textured or embossed elements to add a tactile dimension to the stationery. Custom Illustrations: Include custom illustrations or graphics that convey the essence of the commercial real estate industry or your company's mission and values. Watermark or Background Pattern: Consider adding a subtle watermark or background pattern that complements the overall design without distracting from the content. Custom Typography: Explore the use of custom typography or stylized lettering for headers or key text elements to make the stationery more visually appealing. Enhanced Print Options: If budget allows, opt for premium printing techniques like foil stamping, spot UV, or letterpress to make the stationery truly stand out. Digital Templates: Request digital templates for electronic documents, such as Microsoft Word templates, PowerPoint templates, or PDF templates, to maintain consistency in digital communications. Multiple Design Concepts: Ask for variations of the stationery design to choose from, providing you with options for different occasions or purposes. QR Codes: If relevant, consider incorporating QR codes that link to Vostrana's website, portfolio, or contact information for convenient access. Environmentally Friendly Options: Explore eco-friendly printing materials and practices to align with sustainability goals, if applicable. Mobile Optimization: Ensure that any digital templates or elements are optimized for mobile use, enhancing accessibility and usability. Social Media Icons: Include social media icons and links to Vostrana's social media profiles, if desired, for a comprehensive online presence. Alternate Color Schemes: Request variations of the design with alternate color schemes for seasonal or special occasions.
Should not have
• Non-Compliance with Brand Guidelines: Specify that the design must strictly adhere to Vostrana's brand guidelines, and any deviations are not acceptable. Excessive Complexity: Avoid overly complex designs that may clutter the stationery or distract from the essential information. Inconsistent Branding: Ensure that all design elements, including colors, fonts, and logo usage, remain consistent with the provided brand standards. Unapproved Fonts: Specify that designers should only use the approved fonts from the brand guidelines and avoid introducing new fonts. Inappropriate Imagery: Request that designers refrain from using images, illustrations, or graphics that are unrelated to the Commercial Real Estate industry or that could potentially be perceived as unprofessional. Overly Bright Colors: If it doesn't align with your brand, discourage the use of overly bright or neon colors that may not convey professionalism. Clashing Color Schemes: Ensure that the color scheme chosen for the design is harmonious and avoids color combinations that clash or are difficult to read. Overuse of Effects: Discourage excessive use of visual effects, such as gradients, drop shadows, or excessive transparency, which can make the stationery appear cluttered. Extravagant Printing Costs: Specify that designers should consider budget constraints and avoid design elements that would significantly increase printing costs, unless the budget allows for premium printing techniques. Outdated Design Trends: Request that the design avoids incorporating outdated design trends that may make the stationery appear dated. Inconsistent Branding Across Items: Ensure that the design maintains consistency across all stationery items (letterhead, business cards, envelopes, etc.) and that there are no significant variations that could create confusion. Overly Busy Layouts: Ask for designs that have a clean and professional appearance, avoiding overcrowded layouts that make it difficult to read or find essential information.

```html
<!DOCTYPE html>
<html lang="en">
<head>
<meta charset="utf-8">
<title>Vostrana Corporate Stationery</title>
<link rel="stylesheet" href="https://fonts.googleapis.com/css2?family=Figtree:wght@400;600;700;800&family=Open+Sans:wght@400&family=Montserrat:wght@700&display=swap">
<style>
  :root {
    --navy: #021e4c;
    --board: #a4a4a4;
    --paper: #ffffff;
    --ink: #333a44;
    --muted: #7a7f88;
    --pencil-tip: #f6e7a6;
  }
  * { margin: 0; padding: 0; box-sizing: border-box; }
  html, body { width: 1200px; height: 1200px; overflow: hidden; background: var(--paper); }
  body { position: relative; font-family: "Figtree", sans-serif; color: var(--navy); }
  .board { position: absolute; left: 1px; top: 109px; width: 1197px; height: 984px; background: var(--board); }
  .item { position: absolute; background: var(--paper); overflow: hidden; }
  .abs { position: absolute; }
  .band { position: absolute; left: 0; right: 0; bottom: 0; background: var(--navy); }
  .brand-name { font-family: "Figtree", sans-serif; font-weight: 800; color: var(--navy); letter-spacing: 0.12em; text-transform: uppercase; white-space: nowrap; }
  .brand-name.light { color: var(--paper); }
  .company { font-weight: 700; font-size: 8px; color: var(--navy); }
  .address { font-size: 8px; color: var(--muted); line-height: 11px; letter-spacing: 0.02em; }
  .contact { font-size: 8px; color: var(--paper); line-height: 11px; display: flex; align-items: center; gap: 4px; white-space: nowrap; }
  .contact svg { width: 6px; height: 6px; fill: var(--paper); flex: none; }

  /* bag */
  .bag-handle { position: absolute; left: 145px; top: 188px; width: 196px; height: 170px; border: 11px solid var(--navy); border-radius: 50%; }
  .bag { left: 62px; top: 265px; width: 357px; height: 500px; }
  .bag .band { height: 49px; }

  /* letterhead */
  .letterhead { left: 471px; top: 265px; width: 386px; height: 493px; }
  .letterhead .band { height: 82px; }
  .person { font-weight: 700; font-size: 12.5px; color: var(--navy); }
  .role { font-size: 8px; color: var(--muted); }
  .date { font-weight: 700; font-size: 9.5px; color: #1b1f28; }
  .letter-body { position: absolute; left: 29px; top: 193px; width: 328px; font-family: "Open Sans", sans-serif; font-size: 6.7px; line-height: 8.05px; color: var(--ink); text-align: justify; letter-spacing: 0.03em; }
  .letter-body p { margin-bottom: 5px; }
  .sign-line { position: absolute; left: 29px; top: 388px; width: 70px; height: 1.5px; background: var(--navy); }
  .sign-label { position: absolute; left: 45px; top: 394px; font-weight: 700; font-size: 7.5px; color: #1b1f28; }

  /* pencil */
  .pencil { position: absolute; left: 995px; top: 295px; width: 16px; height: 345px; }
  .pencil-body { position: absolute; left: 0; top: 23px; width: 16px; height: 322px; background: linear-gradient(90deg, #ffffff 60%, #d7d7d7); }
  .pencil-label { position: absolute; left: 8px; top: 330px; transform-origin: left top; transform: rotate(-90deg); font-weight: 700; font-size: 6px; color: var(--navy); white-space: nowrap; }

  /* envelope */
  .envelope { left: 62px; top: 804px; width: 387px; height: 209px; border-radius: 14px 14px 0 0; }

  /* compliments slip */
  .slip { left: 471px; top: 830px; width: 399px; height: 172px; }
  .slip .band { height: 55px; }

  /* business cards */
  .card-front { left: 897px; top: 708px; width: 241px; height: 137px; }
  .card-back { left: 897px; top: 865px; width: 241px; height: 137px; background: var(--navy); }
  .card-back .person { color: var(--paper); font-size: 11px; }
  .card-back .role { color: var(--paper); font-size: 6.5px; }
  .card-back .company { color: var(--paper); font-size: 6px; }
  .card-back .address, .card-back .contact { color: var(--paper); font-size: 6.3px; line-height: 8.5px; }
  .card-back .contact svg { width: 5px; height: 5px; }
</style>
</head>
<body>
  <div class="board"></div>

  <!-- shopping bag -->
  <div class="bag-handle"></div>
  <section class="item bag">
    <div class="brand-name abs" style="left:0;right:0;top:242px;text-align:center;font-size:36px;">Vostrana</div>
    <div class="band">
      <div class="brand-name light abs" style="left:0;right:0;top:18px;text-align:center;font-size:11px;">Vostrana</div>
    </div>
  </section>

  <!-- letterhead -->
  <section class="item letterhead">
    <div class="brand-name abs" style="left:28px;top:73px;font-size:16px;">Vostrana</div>
    <div class="abs" style="left:228px;top:60px;">
      <div class="company">Vostrana Commercial Real Estate</div>
      <div class="address">4270 Harbor Crest Drive, Suite 310,<br>Lakemont, CA 90417</div>
    </div>
    <div class="abs" style="left:29px;top:140px;">
      <div class="person">Marcus Ellery</div>
      <div class="role">Founder &amp; Director</div>
    </div>
    <div class="date abs" style="left:268px;top:170px;">Date:</div>
    <div class="letter-body">
      <p>Lorem Ipsum is simply dummy text of the printing and typesetting industry. Lorem Ipsum has been the industry's standard dummy text ever since the 1500s, when an unknown printer took a galley of type and scrambled it to make a type specimen book. It has survived not only five centuries, but also the leap into electronic typesetting, remaining essentially unchanged. It was popularised in the 1960s with the release of Typeline sheets containing Lorem Ipsum passages, and more recently with desktop publishing software like PageForge including versions of Lorem Ipsum.</p>
      <p>It is a long established fact that a reader will be distracted by the readable content of a page when looking at its layout. The point of using Lorem Ipsum is that it has a more-or-less normal distribution of letters, as opposed to using 'Content here, content here', making it look like readable English. Many desktop publishing packages and web page editors now use Lorem Ipsum as their default model text, and a search for 'lorem ipsum' will uncover many web sites still in their infancy. Various versions have evolved over the years, sometimes by accident, sometimes on purpose (injected humour and the like).</p>
      <p>Contrary to popular belief, Lorem Ipsum is not simply random text. It has roots in a piece of classical Latin literature from 45 BC, making it over 2000 years old. Daniel Ashcombe, a Latin professor at Westbrook College in Virginia, looked up one of the more obscure Latin words, consectetur, from a Lorem Ipsum passage, and going through the cites of the word in classical literature, discovered the undoubtable source.</p>
    </div>
    <div class="sign-line"></div>
    <div class="sign-label">Signeture</div>
    <div class="band">
      <div class="abs" style="left:29px;top:30px;">
        <div class="contact"><svg viewBox="0 0 10 10"><path d="M2 0.5l2 2-1 1.3c.6 1.3 1.6 2.3 2.9 2.9l1.3-1 2 2-1.5 1.8C4 9 1 6 .2 2z"/></svg>(555)-304-7720</div>
        <div class="contact"><svg viewBox="0 0 10 10"><path d="M0 2h10v6H0z M0 2l5 3.5L10 2" stroke="#021e4c" stroke-width="0.8"/></svg>info@vostranacre.com</div>
      </div>
      <div class="brand-name light abs" style="left:0;right:0;top:34px;text-align:center;font-size:12px;">Vostrana</div>
      <div class="abs" style="left:277px;top:30px;">
        <div class="contact"><svg viewBox="0 0 10 10"><circle cx="5" cy="5" r="4.5"/><path d="M0.5 5h9M5 .5v9M2 2.5c2 1 4 1 6 0M2 7.5c2-1 4-1 6 0" stroke="#021e4c" stroke-width="0.7" fill="none"/></svg>www.vostrana.com</div>
        <div class="contact"><svg viewBox="0 0 10 10"><rect x="1" y="1" width="8" height="8" rx="2"/></svg>Vostrana</div>
      </div>
    </div>
  </section>

  <!-- pencil -->
  <div class="pencil">
    <svg class="abs" style="left:0;top:0;" width="16" height="24" viewBox="0 0 16 24"><path d="M8 0L16 23H0z" fill="var(--pencil-tip)"/><path d="M8 0l2.6 7.5H5.4z" fill="#111"/></svg>
    <div class="pencil-body"></div>
    <div class="pencil-label">Vostrana Commercial Real Estate</div>
  </div>

  <!-- envelope -->
  <section class="item envelope">
    <svg class="abs" style="left:0;top:0;" width="387" height="52" viewBox="0 0 387 52"><path d="M0 14Q0 0 18 0H369Q387 0 387 14V31L335 52H52L0 31z" fill="var(--navy)"/></svg>
    <div class="brand-name abs" style="left:303px;top:146px;font-size:10px;">Vostrana</div>
  </section>

  <!-- compliments slip -->
  <section class="item slip">
    <div class="brand-name abs" style="left:30px;top:52px;font-size:11px;">Vostrana</div>
    <div class="abs" style="left:241px;top:40px;">
      <div class="company">Vostrana Commercial Real Estate</div>
      <div class="address">4270 Harbor Crest Drive, Suite 310,<br>Lakemont, CA 90417</div>
    </div>
    <div class="band">
      <div class="abs" style="left:31px;top:18px;">
        <div class="contact"><svg viewBox="0 0 10 10"><path d="M2 0.5l2 2-1 1.3c.6 1.3 1.6 2.3 2.9 2.9l1.3-1 2 2-1.5 1.8C4 9 1 6 .2 2z"/></svg>(555)-304-7720</div>
        <div class="contact"><svg viewBox="0 0 10 10"><path d="M0 2h10v6H0z M0 2l5 3.5L10 2" stroke="#021e4c" stroke-width="0.8"/></svg>info@vostranacre.com</div>
      </div>
      <div class="brand-name light abs" style="left:0;right:0;top:22px;text-align:center;font-size:10px;">Vostrana</div>
      <div class="abs" style="left:288px;top:18px;">
        <div class="contact"><svg viewBox="0 0 10 10"><circle cx="5" cy="5" r="4.5"/><path d="M0.5 5h9M5 .5v9M2 2.5c2 1 4 1 6 0M2 7.5c2-1 4-1 6 0" stroke="#021e4c" stroke-width="0.7" fill="none"/></svg>www.vostrana.com</div>
        <div class="contact"><svg viewBox="0 0 10 10"><rect x="1" y="1" width="8" height="8" rx="2"/></svg>Vostrana</div>
      </div>
    </div>
  </section>

  <!-- business card front -->
  <section class="item card-front">
    <div class="brand-name abs" style="left:0;right:0;top:62px;text-align:center;font-size:15px;">Vostrana</div>
  </section>

  <!-- business card back -->
  <section class="item card-back">
    <div class="abs" style="left:18px;top:11px;">
      <div class="person">Marcus Ellery</div>
      <div class="role">Founder &amp; Director</div>
    </div>
    <div class="abs" style="left:18px;top:58px;">
      <div class="company">Vostrana Commercial Real Estate</div>
      <div class="address">4270 Harbor Crest Drive, Suite 310,<br>Lakemont, CA 90417</div>
      <div class="contact" style="margin-top:2px;"><svg viewBox="0 0 10 10"><path d="M2 0.5l2 2-1 1.3c.6 1.3 1.6 2.3 2.9 2.9l1.3-1 2 2-1.5 1.8C4 9 1 6 .2 2z"/></svg>(555)-304-7720</div>
      <div class="contact"><svg viewBox="0 0 10 10"><path d="M0 2h10v6H0z M0 2l5 3.5L10 2" stroke="#021e4c" stroke-width="0.8"/></svg>info@vostranacre.com</div>
      <div class="contact"><svg viewBox="0 0 10 10"><circle cx="5" cy="5" r="4.5"/><path d="M0.5 5h9M5 .5v9M2 2.5c2 1 4 1 6 0M2 7.5c2-1 4-1 6 0" stroke="#021e4c" stroke-width="0.7" fill="none"/></svg>www.vostrana.com</div>
      <div class="contact"><svg viewBox="0 0 10 10"><rect x="1" y="1" width="8" height="8" rx="2"/></svg>@Vostrana</div>
    </div>
    <div class="brand-name light abs" style="left:152px;top:62px;font-size:11px;">Vostrana</div>
  </section>
</body>
</html>
```